Business Cards for IT Consulting Company (Managed Service Provider)

I am looking to have some business cards printed and would like some designs. We are an IT Consulting company based in Vancouver BC. I would like a nice clean and modern look to the cards. I have uploaded all the versions of my logo so parts can be used as needed. Here is a snippit from our website homepage:

Kelbrook Systems Ltd. is an IT Solutions Partner located in Vancouver BC, Canada. We offer IT solutions and support to customers in the greater Vancouver Area. With expertise in Microsoft platforms, as well as Linux and Mac OSX and over 12 years experience in the IT industry, Kelbrook Systems is dedicated to offering our clients top quality service and products. We take pride in the solutions we offer our customers. The greatest compliment a client can give us is to recommend our services.

Kelbrook Systems Ltd. offers a wide range of IT services from onsite service to remote support and managed service solutions. This allows clients to choose the support path that best suits their company’s needs. Supporting many different sized companies from small to enterprise level over the past 12 years Kelbrook Systems has the experience and expertise needed to ensure things run smoothly. Allowing our clients to focus on doing business.

Revolutionizing the way IT services are delivered.

Kelbrook Systems is dedicated to providing our clients with IT solutions that work and grow with them for years to come. This philosophy helps save money in the long run instead of replacing equipment constantly. Far too often IT solutions are not well thought out and while possibly solving the problem at hand, require replacement due to growth or quality within a very short time frame. Kelbrook Systems takes pride in providing solutions that will last and be able to accommodate growth without the need for replacement.

Industry/Entity Type

Information Technology

Contact Information for Business Card

Kelbrook Systems Ltd.
(Employee Name)
Eml: (Employees Email Address)
Web: kelbrook.me
Ph: 604-555-0142

Font styles to use
Serif
Sans Serif

Requirements
Must have
• The Company logo and company colors.
Nice to have
• - Our tag line: "Reliable IT, Built to Last" or "Revolutionizing the way IT services are delivered."
• - Also I really like the idea of nature and technology together blending which is sort of where my logo came from so integrating that somehow onto the business cards would be great.

```html
<!DOCTYPE html>
<html lang="en">
<head>
<meta charset="utf-8">
<title>Kelbrook Systems Business Cards</title>
<link rel="stylesheet" href="https://fonts.googleapis.com/css2?family=Lato:wght@400;700&family=Montserrat:wght@600&display=swap">
<style>
  :root {
    --stage: #2b2b2d;
    --card-white: #f6f7f8;
    --card-dark: #231f20;
    --brand-blue: #2e9ad8;
    --text-light: #d9d9d9;
    --text-muted: #a9a9a9;
    --photo-warm: #8a6a3a;
    --photo-teal: #2d4a4c;
    --photo-night: #1c2426;
  }
  * { box-sizing: border-box; margin: 0; padding: 0; }
  html, body { width: 1200px; height: 997px; overflow: hidden; }
  body {
    background: var(--stage);
    font-family: "Lato", Arial, sans-serif;
    position: relative;
  }
  .card {
    position: absolute;
    width: 520px;
    height: 300px;
    top: 348px;
    overflow: hidden;
    box-shadow: 0 10px 30px rgba(0,0,0,.45);
  }
  /* Front */
  .card--front { left: 50px; background: var(--card-dark); }
  .front__top {
    position: absolute; inset: 0 0 auto 0; height: 128px;
    background: var(--card-white);
    border-bottom: 4px solid var(--brand-blue);
  }
  .front__notch { position: absolute; left: 30px; top: 128px; }
  .brand {
    position: absolute; left: 54px; top: 44px;
    display: flex; align-items: center; gap: 14px;
  }
  .brand__mark { width: 34px; height: 34px; border: 3px solid var(--brand-blue); }
  .brand__name {
    font-family: "Lato", Arial, sans-serif; font-weight: 700;
    font-size: 36px; color: var(--brand-blue); letter-spacing: .5px;
  }
  .person { position: absolute; left: 28px; top: 168px; }
  .person__name { color: var(--brand-blue); font-size: 17px; }
  .person__role { color: var(--text-light); font-size: 12px; margin-top: 3px; }
  .company { position: absolute; left: 28px; top: 236px; }
  .company__name { color: var(--brand-blue); font-size: 13px; font-weight: 700; }
  .company__address { color: var(--text-muted); font-size: 11px; margin-top: 5px; }
  .contact {
    position: absolute; right: 18px; top: 150px;
    display: flex; flex-direction: column; align-items: flex-end; gap: 10px;
  }
  .contact__row { display: flex; align-items: center; gap: 8px; color: var(--text-light); font-size: 12px; }
  .contact__icon { width: 12px; height: 12px; }
  .front__base { position: absolute; left: 0; right: 0; bottom: 0; height: 5px; background: var(--brand-blue); }
  /* Back */
  .card--back { left: 630px; }
  .back__photo {
    position: absolute; inset: 0;
    background:
      radial-gradient(ellipse at 50% 0%, var(--photo-warm) 0%, transparent 55%),
      linear-gradient(160deg, var(--photo-teal) 0%, var(--photo-night) 100%);
  }
  .back__lockup {
    position: absolute; left: 0; right: 0; top: 92px; text-align: center;
  }
  .back__name {
    font-family: "Lato", Arial, sans-serif; font-weight: 700;
    font-size: 38px; color: #fff;
  }
  .back__tagline {
    font-family: "Montserrat", Arial, sans-serif; font-weight: 600;
    font-size: 13px; letter-spacing: 2px; color: #fff; margin-top: 8px;
  }
  .back__web {
    position: absolute; left: 0; right: 0; bottom: 0; height: 50px;
    background: rgba(0,0,0,.45);
    display: flex; align-items: center; justify-content: center;
    font-family: "Montserrat", Arial, sans-serif; font-weight: 600;
    font-size: 15px; letter-spacing: 4px; color: #fff;
  }
</style>
</head>
<body>
  <section class="card card--front">
    <div class="front__top">
      <div class="brand">
        <span class="brand__mark"></span>
        <span class="brand__name">Kelbrook Systems</span>
      </div>
    </div>
    <svg class="front__notch" width="34" height="14" viewBox="0 0 34 14">
      <polygon points="0,0 34,0 17,12" fill="var(--brand-blue)"/>
    </svg>
    <div class="person">
      <p class="person__name">Dana Morlan</p>
      <p class="person__role">Network Engineer</p>
    </div>
    <div class="company">
      <p class="company__name">Kelbrook Systems Ltd</p>
      <p class="company__address">218 Harbour Lane, Vancouver BC, Canada</p>
    </div>
    <div class="contact">
      <div class="contact__row">604-555-0142
        <svg class="contact__icon" viewBox="0 0 12 12"><rect x="2.5" y="0.5" width="7" height="11" rx="1.5" fill="none" stroke="var(--brand-blue)"/></svg>
      </div>
      <div class="contact__row">dmorlan@kelbrook.me
        <svg class="contact__icon" viewBox="0 0 12 12"><rect x="0.5" y="2.5" width="11" height="7" fill="var(--brand-blue)"/><polyline points="0.5,2.5 6,6.5 11.5,2.5" fill="none" stroke="var(--card-dark)"/></svg>
      </div>
    </div>
    <div class="front__base"></div>
  </section>

  <section class="card card--back">
    <div class="back__photo" role="img" aria-label="Aerial photograph of a downtown city at dusk with glowing streets and the harbour"></div>
    <div class="back__lockup">
      <p class="back__name">Kelbrook Systems</p>
      <p class="back__tagline">Reliable IT, Built to Last</p>
    </div>
    <div class="back__web">www.kelbrook.me</div>
  </section>
</body>
</html>
```